Driftwood Bay Private Yacht Charter "Rack Flyer"

This will be a 4" x 9" Rack flyer that is 4 colors and two sided. This is a Private Yacht charter company that is based in St Thomas, U.S. Virgin Islands. Our main product that I would like to promote on one entire side of the flyer is our Private Luxury Full Day "Gilded Galley". our charter company is unique in the fact we offer customizable itineraries and we offer unique activities that keep the family and groups engaged in fun for the entire day. We would like something with our colors.

Target Market(s)

We are trying to reach an upscale clients that are looking for a Luxury Day Charter experience. these people will be most likely staying in Private Villas or staying at the Halloway Crest or PK Bellmont.

Requirements
Must have
• Contact Information:
Ph: (340) 555-0187
email: Info@driftwoodbayvoyages.example
www.driftwoodbayvoyages.example
One side should Promote our Gilded Galley (Gilded Galley is a trademarked name).
All Guests will receive "Harbor Fizz"
> Up to 12 guests
> Full Brunch Spread to include, Assorted fruit tower, Artesian Waffle Board, Frittata's, Loaded Avocado Toast or an All American Breakfast.
> Specialty Cocktails with Bottle Service options available
List all of our Unique activities to include:
Snorkeling
Underwater WaveGlider
Cliff Diving
Paddleboarding
Towable Activities
TEXT TO BE WRITTEN:
Experience yacht charter service at its Finest!
Sail away with us on a Luxury Charter experience complete with a full brunch spread. During our sail we will take you to the hottest destination spots in the Caribbean surrounding St Thomas and St John. Warm, fresh baked afternoon cookies will be served on the way back from our days journeys. Unlimited water, sodas, beer and rum punch will be provided for the entire group to enjoy throughout the day.
_________________

On side two of the brochure you can refer to the downloaded text. We do not want pricing listed on the flyer

```html
<!DOCTYPE html>
<html lang="en">
<head>
<meta charset="UTF-8">
<title>Driftwood Bay Private Yacht Charter – Rack Flyer</title>
<link href="https://fonts.googleapis.com/css2?family=Great+Vibes&family=Montserrat:wght@400;500;700;800&family=Oswald:wght@600&display=swap" rel="stylesheet">
<style>
  :root {
    --stage: #5e5b5b;
    --paper: #ffffff;
    --brand-red: #e12a31;
    --brand-blue: #1d4f9e;
    --ink: #1b1b1b;
    --muted: #444444;
    --sea-deep: #1a9bb7;
    --sea-light: #7fd3df;
    --sky: #cfe4ee;
    --sand: #e9d6b0;
    --frame: #ffffff;
  }
  * { box-sizing: border-box; margin: 0; padding: 0; }
  html, body { width: 1200px; height: 2358px; overflow: hidden; }
  body { background: var(--stage); position: relative; font-family: 'Montserrat', sans-serif; color: var(--ink); }

  .flyer {
    position: absolute; left: 172px; top: 216px;
    width: 856px; height: 1925px;
    background: var(--paper); overflow: hidden;
  }

  .hero-photo {
    position: absolute; left: 0; top: 0; width: 856px; height: 440px;
    background:
      linear-gradient(to bottom, rgba(255,255,255,0) 70%, var(--paper) 100%),
      linear-gradient(to bottom, var(--sky) 0%, #9fc9d6 25%, #6b9a6a 42%, var(--sea-deep) 60%, #3cb6cc 80%, #d9ebe8 100%);
  }

  .sea-photo {
    position: absolute; left: 0; top: 900px; width: 856px; height: 670px;
    background: linear-gradient(to bottom, rgba(255,255,255,0) 0%, rgba(160,220,228,0.7) 22%, var(--sea-light) 40%, #35aec3 70%, var(--sea-deep) 100%);
  }

  .framed {
    position: absolute;
    border: 14px solid var(--frame);
    box-shadow: 0 6px 14px rgba(0,0,0,0.35);
  }
  .framed--yacht {
    left: -20px; top: -40px; width: 420px; height: 310px; transform: rotate(-8deg);
    background: linear-gradient(160deg, var(--sand) 0%, #d7c49c 25%, #5fc9d8 45%, #1da7c2 100%);
  }
  .framed--snorkel {
    left: 425px; top: 1240px; width: 400px; height: 345px; transform: rotate(4deg);
    background: linear-gradient(135deg, #2aa9c6 0%, #1b8fae 50%, #3fc0d3 100%);
  }
  .framed--island {
    left: 520px; top: 1520px; width: 400px; height: 350px; transform: rotate(-12deg);
    background: linear-gradient(to bottom, #d7e8f0 0%, #7fc6e0 30%, #22a5cc 55%, #3f8f3d 80%, #2f7a2c 100%);
  }

  .headline {
    position: absolute; left: 66px; top: 396px; width: 790px;
    font-family: 'Great Vibes', cursive; font-weight: 400;
    font-size: 102px; line-height: 92px; color: var(--brand-red);
  }

  .copy {
    position: absolute; left: 77px; width: 720px;
    font-size: 26px; line-height: 38.6px; font-weight: 400;
  }
  .copy--intro { top: 606px; text-indent: 32px; }
  .copy--why { top: 985px; }
  .why-title {
    position: absolute; left: 77px; top: 940px;
    font-size: 30px; font-weight: 800; color: #000;
  }

  .contact-band {
    position: absolute; left: 0; top: 1568px; width: 856px; height: 357px;
    background: var(--paper);
  }

  .brand-name {
    position: absolute; left: 50px; top: 1624px;
    display: flex; align-items: center; gap: 12px;
    font-size: 44px; font-weight: 700; color: var(--brand-red);
  }
  .brand-name .dot {
    width: 20px; height: 20px; border-radius: 50%; background: var(--brand-blue);
  }

  .book-button {
    position: absolute; left: 44px; top: 1718px; width: 332px; height: 38px;
    background: var(--brand-blue); color: #fff;
    font-size: 22px; font-weight: 500; line-height: 38px; text-align: center;
  }

  .phone {
    position: absolute; left: 36px; top: 1762px;
    display: flex; align-items: center; gap: 8px;
    font-family: 'Oswald', sans-serif; font-weight: 600;
    font-size: 60px; line-height: 70px; color: var(--brand-red);
  }
  .phone svg { width: 46px; height: 52px; }

  .contact-line {
    position: absolute; left: 92px;
    display: flex; align-items: center; gap: 9px;
    font-size: 21px; color: var(--muted);
  }
  .contact-line svg { width: 20px; height: 20px; }
  .contact-line--email { top: 1846px; }
  .contact-line--web { top: 1877px; }
</style>
</head>
<body>
  <main class="flyer">
    <div class="hero-photo" role="img" aria-label="Two children with raised arms overlooking a turquoise bay with moored sailboats"></div>
    <div class="framed framed--yacht" role="img" aria-label="White catamaran anchored off a sandy beach"></div>

    <h1 class="headline">Experience yacht charter<br>service at its Finest!</h1>

    <p class="copy copy--intro">Sail away with us on a Luxury Charter experience complete with a full brunch spread. During our sail we will take you to the hottest destination spots in the Caribbean surrounding St Thomas and St John. Warm, fresh baked afternoon cookies will be served on the way back from our days journeys. Unlimited water, sodas, beer and rum punch will be provided for the entire group to enjoy throughout the day.</p>

    <div class="sea-photo" role="img" aria-label="Aerial view of a catamaran on clear turquoise water beside breaking surf"></div>

    <h2 class="why-title">Why Driftwood Bay?</h2>
    <p class="copy copy--why">Driftwood Bay will be sure to give you the experience of a lifetime. Chartering with us is a great experience for the whole group. With our flexible offerings, the possibilities are endless when it comes to having fun on one of the newest private yachts in the caribbean. Enjoy various activities as well as relaxation.</p>

    <div class="framed framed--snorkel" role="img" aria-label="Snorkeler swimming underwater over a sandy reef"></div>

    <section class="contact-band"></section>

    <div class="framed framed--island" role="img" aria-label="Green island hillside above a turquoise bay and white beach"></div>

    <div class="brand-name"><span>Driftwood Bay</span><span class="dot"></span></div>

    <div class="book-button">BOOK YOUR TOUR NOW!!</div>

    <div class="phone">
      <svg viewBox="0 0 50 56" aria-hidden="true">
        <rect x="14" y="4" width="26" height="48" rx="5" fill="none" stroke="var(--brand-red)" stroke-width="5"/>
        <rect x="20" y="42" width="14" height="4" fill="var(--brand-red)"/>
        <path d="M4 18 Q2 28 4 40 L12 38 L12 20 Z" fill="var(--brand-red)"/>
      </svg>
      <span>(340) 555-0187</span>
    </div>

    <div class="contact-line contact-line--email">
      <svg viewBox="0 0 22 22" aria-hidden="true">
        <rect x="2" y="4" width="18" height="14" fill="none" stroke="var(--brand-red)" stroke-width="2"/>
        <path d="M2 5 L11 12 L20 5" fill="none" stroke="var(--brand-red)" stroke-width="2"/>
      </svg>
      <span>Info@driftwoodbayvoyages.example</span>
    </div>
    <div class="contact-line contact-line--web">
      <svg viewBox="0 0 22 22" aria-hidden="true">
        <circle cx="11" cy="11" r="9" fill="none" stroke="var(--brand-red)" stroke-width="2"/>
        <ellipse cx="11" cy="11" rx="4" ry="9" fill="none" stroke="var(--brand-red)" stroke-width="2"/>
        <path d="M2 11 H20" stroke="var(--brand-red)" stroke-width="2"/>
      </svg>
      <span>www.driftwoodbayvoyages.example</span>
    </div>
  </main>
</body>
</html>
```